Trailer wrap for home remodeling company in Sarasota County Florida

I need a wrap design for an enclosed trailer. I like the idea of adding a picture of a really nice kitchen or bathroom, possibly a before and after.
Matte black background
Must include the below information
Pelican Crest Remodeling
CGC2807391
941-555–0187
www.pelicancrestremodeling.example
Bathrooms,Kitchens, Additions, Remodels
Trusted Expertise. Refined Design
Trailer is currently all black
Updates

Designs are not what we are looking for, very busy

Industry/Entity Type

Home Remodeling

Colors
0054AA
0677BA
7BADD7
CADEEF
E8F1F8

Requirements
Must have
• Matte black background

```html
<!DOCTYPE html>
<html lang="en">
<head>
<meta charset="utf-8">
<title>Pelican Crest Remodeling – Trailer Wrap</title>
<link rel="stylesheet" href="https://fonts.googleapis.com/css2?family=Cormorant+Garamond:wght@500&family=Oswald:wght@400;600&family=Poppins:wght@500;600&family=Saira+Condensed:wght@700&display=swap">
<style>
  :root{
    --matte:#101112;
    --charcoal:#2a2b2d;
    --royal:#0054AA;
    --ocean:#0677BA;
    --sky:#7BADD7;
    --mist:#CADEEF;
    --frost:#E8F1F8;
    --silver:#d9dcdf;
    --white:#ffffff;
    --stage:#eceef0;
  }
  html,body{margin:0;padding:0;overflow:hidden;}
  body{width:1200px;height:2399px;background:var(--stage);position:relative;}
  .wrap-side{position:absolute;left:50px;width:1100px;height:560px;}
  .wrap-side--driver{top:120px;}
  .wrap-side--curb{top:920px;}
  .wrap-front{position:absolute;top:1690px;width:300px;height:640px;}
  .wrap-front--left{left:270px;}
  .wrap-front--right{left:630px;}
  svg{display:block;}
  .brand-name{font-family:"Cormorant Garamond",serif;font-weight:500;fill:var(--white);letter-spacing:3px;}
  .tagline{font-family:"Oswald",sans-serif;font-weight:400;fill:var(--white);}
  .tagline-accent{font-weight:600;font-style:italic;fill:var(--ocean);}
  .license{font-family:"Poppins",sans-serif;font-weight:500;fill:var(--white);}
  .phone{font-family:"Saira Condensed",sans-serif;font-weight:700;fill:var(--silver);}
  .phone--blue{fill:var(--ocean);}
  .web{font-family:"Poppins",sans-serif;font-weight:500;fill:var(--white);}
  .service{font-family:"Poppins",sans-serif;font-weight:600;fill:var(--matte);}
  .service-chip{font-family:"Poppins",sans-serif;font-weight:500;fill:var(--white);}
</style>
</head>
<body>

<svg width="0" height="0" style="position:absolute">
  <defs>
    <linearGradient id="photo-tones" x1="0" y1="0" x2="0" y2="1">
      <stop offset="0" stop-color="#e7e9ea"/>
      <stop offset=".45" stop-color="#b8a88f"/>
      <stop offset="1" stop-color="#c9d4de"/>
    </linearGradient>
    <linearGradient id="gray-panel" x1="0" y1="0" x2="1" y2="1">
      <stop offset="0" stop-color="#f2f3f4"/>
      <stop offset="1" stop-color="#c4c8cc"/>
    </linearGradient>
    <linearGradient id="blue-band" x1="0" y1="0" x2="1" y2="0">
      <stop offset="0" stop-color="#0054AA"/>
      <stop offset="1" stop-color="#0677BA"/>
    </linearGradient>
    <linearGradient id="blue-base" x1="0" y1="0" x2="1" y2="1">
      <stop offset="0" stop-color="#0677BA"/>
      <stop offset="1" stop-color="#2a9ad0"/>
    </linearGradient>
  </defs>
</svg>

<!-- Driver side: services left, brand right -->
<svg class="wrap-side wrap-side--driver" viewBox="0 0 1100 560">
  <rect width="1100" height="560" fill="var(--matte)"/>
  <polygon points="0,0 480,0 700,560 0,560" fill="url(#gray-panel)"/>
  <rect x="0" y="0" width="210" height="460" fill="url(#photo-tones)" role="img" aria-label="Photo strip of a finished bathroom, a modern kitchen and renovation plans"/>
  <polygon points="0,440 0,560 300,560" fill="url(#blue-base)"/>
  <polygon points="420,560 560,320 700,560" fill="url(#blue-base)"/>
  <polygon points="440,0 500,0 720,560 660,560" fill="var(--royal)"/>
  <polygon points="500,0 520,0 740,560 720,560" fill="var(--ocean)"/>
  <polygon points="520,0 1100,0 1100,340 650,340" fill="var(--matte)"/>
  <g stroke="#9aa0a6" stroke-width="1">
    <line x1="230" y1="145" x2="440" y2="145"/>
    <line x1="230" y1="255" x2="440" y2="255"/>
    <line x1="230" y1="365" x2="440" y2="365"/>
  </g>
  <text class="service" x="335" y="100" font-size="24" text-anchor="middle">Bathrooms</text>
  <text class="service" x="335" y="210" font-size="24" text-anchor="middle">Kitchens</text>
  <text class="service" x="335" y="320" font-size="24" text-anchor="middle">Additions</text>
  <text class="service" x="335" y="430" font-size="24" text-anchor="middle">Remodels</text>

  <rect x="690" y="60" width="48" height="48" fill="var(--white)"/>
  <text class="brand-name" x="755" y="92" font-size="36">PELICAN CREST</text>
  <text class="brand-name" x="820" y="128" font-size="20" letter-spacing="6">REMODELING</text>
  <text class="tagline" x="1060" y="190" font-size="36" text-anchor="end">TRUSTED <tspan class="tagline-accent">EXPERTISE</tspan></text>
  <text class="tagline" x="1060" y="232" font-size="36" text-anchor="end">REFINED <tspan class="tagline-accent">DESIGN</tspan></text>
  <polygon points="790,258 1085,258 1085,292 780,292" fill="var(--charcoal)"/>
  <polygon points="780,258 790,258 780,292 770,292" fill="var(--ocean)"/>
  <text class="license" x="1065" y="281" font-size="15" text-anchor="end">License # CGC2807391</text>

  <polygon points="640,340 1100,340 1100,430 675,430" fill="url(#blue-band)"/>
  <text class="phone" x="1065" y="405" font-size="56" text-anchor="end">941-555–0187</text>
  <polygon points="675,430 1100,430 1100,475 692,475" fill="var(--charcoal)"/>
  <text class="web" x="1065" y="460" font-size="18" text-anchor="end">www.pelicancrestremodeling.example</text>
  <polygon points="692,475 1100,475 1100,560 720,560" fill="url(#blue-base)"/>
</svg>

<!-- Curb side: brand left, services right -->
<svg class="wrap-side wrap-side--curb" viewBox="0 0 1100 560">
  <rect width="1100" height="560" fill="var(--matte)"/>
  <g transform="translate(1100,0) scale(-1,1)">
    <polygon points="0,0 480,0 700,560 0,560" fill="url(#gray-panel)"/>
    <polygon points="0,440 0,560 300,560" fill="url(#blue-base)"/>
    <polygon points="420,560 560,320 700,560" fill="url(#blue-base)"/>
    <polygon points="440,0 500,0 720,560 660,560" fill="var(--royal)"/>
    <polygon points="500,0 520,0 740,560 720,560" fill="var(--ocean)"/>
    <polygon points="520,0 1100,0 1100,340 650,340" fill="var(--matte)"/>
  </g>
  <rect x="890" y="0" width="210" height="460" fill="url(#photo-tones)" role="img" aria-label="Photo strip of a finished bathroom, a modern kitchen and renovation plans"/>
  <rect x="620" y="40" width="215" height="500" fill="none" stroke="#3a3d40" stroke-width="6"/>
  <g stroke="#9aa0a6" stroke-width="1">
    <line x1="650" y1="145" x2="860" y2="145"/>
    <line x1="650" y1="255" x2="860" y2="255"/>
    <line x1="650" y1="365" x2="860" y2="365"/>
  </g>
  <text class="service" x="765" y="100" font-size="24" text-anchor="middle">Bathrooms</text>
  <text class="service" x="765" y="210" font-size="24" text-anchor="middle">Kitchens</text>
  <text class="service" x="765" y="320" font-size="24" text-anchor="middle">Additions</text>
  <text class="service" x="765" y="430" font-size="24" text-anchor="middle">Remodels</text>

  <rect x="40" y="60" width="48" height="48" fill="var(--white)"/>
  <text class="brand-name" x="105" y="92" font-size="36">PELICAN CREST</text>
  <text class="brand-name" x="170" y="128" font-size="20" letter-spacing="6">REMODELING</text>
  <text class="tagline" x="40" y="190" font-size="36">TRUSTED <tspan class="tagline-accent">EXPERTISE</tspan></text>
  <text class="tagline" x="40" y="232" font-size="36">REFINED <tspan class="tagline-accent">DESIGN</tspan></text>
  <polygon points="0,258 305,258 295,292 0,292" fill="var(--charcoal)"/>
  <polygon points="305,258 315,258 305,292 295,292" fill="var(--ocean)"/>
  <text class="license" x="40" y="281" font-size="15">License # CGC2807391</text>

  <polygon points="0,340 460,340 425,430 0,430" fill="url(#blue-band)"/>
  <text class="phone" x="40" y="405" font-size="56">941-555–0187</text>
  <polygon points="0,430 425,430 408,475 0,475" fill="var(--charcoal)"/>
  <text class="web" x="40" y="460" font-size="18">www.pelicancrestremodeling.example</text>
  <polygon points="0,475 408,475 380,560 0,560" fill="url(#blue-base)"/>
</svg>

<!-- Front panels -->
<svg class="wrap-front wrap-front--left" viewBox="0 0 300 640">
  <rect width="300" height="640" fill="var(--matte)"/>
  <rect x="126" y="40" width="48" height="48" fill="var(--white)"/>
  <text class="brand-name" x="150" y="130" font-size="24" text-anchor="middle" letter-spacing="2">PELICAN CREST</text>
  <text class="brand-name" x="150" y="154" font-size="13" text-anchor="middle" letter-spacing="5">REMODELING</text>
  <text class="tagline" x="150" y="196" font-size="24" text-anchor="middle">Trusted <tspan class="tagline-accent">EXPERTISE</tspan></text>
  <text class="tagline" x="150" y="224" font-size="24" text-anchor="middle">Refined <tspan class="tagline-accent">DESIGN</tspan></text>
  <rect x="30" y="248" width="240" height="32" fill="var(--charcoal)"/>
  <text class="license" x="150" y="269" font-size="13" text-anchor="middle">License # CGC2807391</text>
  <g>
    <rect x="65" y="300" width="170" height="30" fill="var(--ocean)"/>
    <text class="service-chip" x="150" y="321" font-size="15" text-anchor="middle">Bathrooms</text>
    <rect x="65" y="342" width="170" height="30" fill="var(--ocean)"/>
    <text class="service-chip" x="150" y="363" font-size="15" text-anchor="middle">Kitchens</text>
    <rect x="65" y="384" width="170" height="30" fill="var(--ocean)"/>
    <text class="service-chip" x="150" y="405" font-size="15" text-anchor="middle">Additions</text>
    <rect x="65" y="426" width="170" height="30" fill="var(--ocean)"/>
    <text class="service-chip" x="150" y="447" font-size="15" text-anchor="middle">Remodels</text>
  </g>
  <text class="phone phone--blue" x="150" y="510" font-size="40" text-anchor="middle">941-555–0187</text>
  <text class="web" x="150" y="536" font-size="11" text-anchor="middle">www.pelicancrestremodeling.example</text>
</svg>

<svg class="wrap-front wrap-front--right" viewBox="0 0 300 640">
  <rect width="300" height="640" fill="var(--matte)"/>
  <rect x="126" y="40" width="48" height="48" fill="var(--white)"/>
  <text class="brand-name" x="150" y="130" font-size="24" text-anchor="middle" letter-spacing="2">PELICAN CREST</text>
  <text class="brand-name" x="150" y="154" font-size="13" text-anchor="middle" letter-spacing="5">REMODELING</text>
  <text class="tagline" x="150" y="196" font-size="24" text-anchor="middle">Trusted <tspan class="tagline-accent">EXPERTISE</tspan></text>
  <text class="tagline" x="150" y="224" font-size="24" text-anchor="middle">Refined <tspan class="tagline-accent">DESIGN</tspan></text>
  <rect x="30" y="248" width="240" height="32" fill="var(--charcoal)"/>
  <text class="license" x="150" y="269" font-size="13" text-anchor="middle">License # CGC2807391</text>
  <g>
    <rect x="65" y="300" width="170" height="30" fill="var(--ocean)"/>
    <text class="service-chip" x="150" y="321" font-size="15" text-anchor="middle">Bathrooms</text>
    <rect x="65" y="342" width="170" height="30" fill="var(--ocean)"/>
    <text class="service-chip" x="150" y="363" font-size="15" text-anchor="middle">Kitchens</text>
    <rect x="65" y="384" width="170" height="30" fill="var(--ocean)"/>
    <text class="service-chip" x="150" y="405" font-size="15" text-anchor="middle">Additions</text>
    <rect x="65" y="426" width="170" height="30" fill="var(--ocean)"/>
    <text class="service-chip" x="150" y="447" font-size="15" text-anchor="middle">Remodels</text>
  </g>
  <text class="phone phone--blue" x="150" y="510" font-size="40" text-anchor="middle">941-555–0187</text>
  <text class="web" x="150" y="536" font-size="11" text-anchor="middle">www.pelicancrestremodeling.example</text>
</svg>

</body>
</html>
```